Icon-Design für Makeup Artist Webseite
Super creative designs. Exactly what we were looking for!Highly recommended.
Zielgruppe
Sabine Ter Horst Makeup Artist. Zielgruppe 18-34. 'Normale' Personen die lernen wollen wie man Makeup richtig aufträgt.
Aufgabenstellung
Das Projekt besteht darin 5 Icons zu designen. Die Webseite ist noch in der Entwicklung ein Screenshot wie es auf dem Handy aussehen soll finden Sie im Anhang.
Es werden 5 creative Icons benötigt die die Kategorien wiederspiegeln.(Also keine "Langweiligen Icone", diese können ruhig ausgefallen sein, sollten jedoch zum style der Seite passen )
Kategorie 1 = Eye Makeup(Lidschatten) Tutorials. Hier sind Texte + Videos enthalten wie man das Augenmakeup richtig aufträgt + Ausgefallene Looks
Kategorie 2 = Skin Care. Texte+Bilder über Haut+Produkte zur richtigen Pflege seiner Haut.
Kategorie 3 = E-Book. Hier steht ein E-Book-Shop zur verfügung indem man sich E-Book kaufen kann.
Kategorie 4 = About. Hier sind alle Informationen über Sabine enthalten.
Download Button = Dieser sollte auf einem leicht grauen-weißen hintergrund ordentlich zum vorschein kommen.
Der Blaue Farb-Code der Webseite ist : 3b5998

```html
<!DOCTYPE html>
<html lang="en">
<head>
<meta charset="utf-8">
<title>Sabine Ter Horst – Mobile Home</title>
<link rel="stylesheet" href="https://fonts.googleapis.com/css2?family=Roboto:wght@400;500;700&family=Open+Sans:wght@400&display=swap">
<style>
  :root {
    --brand-blue: #3b5998;
    --brand-blue-dark: #2f4a8a;
    --logo-gold: #d8b448;
    --stage: #93b3c5;
    --white: #ffffff;
    --blush: #f7d6dd;
    --mist: #e7e7e9;
    --ink: #3d3d3d;
    --lip-1: #c9475a;
    --lip-2: #8e1b2a;
    --skin-1: #d9b8b0;
    --skin-2: #8f6e70;
    --shadow-blue: #a9c8f5;
  }
  * { box-sizing: border-box; margin: 0; padding: 0; }
  html, body { width: 1200px; height: 900px; overflow: hidden; }
  body {
    background: var(--stage);
    font-family: "Roboto", Arial, sans-serif;
    position: relative;
  }
  .screen {
    position: absolute;
    left: 360px; top: 20px;
    width: 480px; height: 860px;
    background: var(--white);
    overflow: hidden;
    box-shadow: 0 0 0 6px var(--white), 0 10px 30px rgba(0,0,0,.2);
  }
  .top-bar {
    height: 100px;
    background: linear-gradient(180deg, var(--brand-blue-dark), var(--brand-blue));
    color: var(--white);
    position: relative;
  }
  .status-bar {
    display: flex; justify-content: space-between; align-items: center;
    height: 28px; padding: 0 10px;
    font-size: 14px;
  }
  .status-bar .battery { display: inline-block; width: 26px; height: 11px; border: 1px solid var(--white); margin-left: 4px; vertical-align: -1px; position: relative; }
  .status-bar .battery::before { content: ""; position: absolute; left: 1px; top: 1px; width: 5px; height: 7px; background: var(--white); }
  .menu-toggle { position: absolute; left: 14px; top: 52px; width: 40px; }
  .menu-toggle span { display: block; height: 3px; background: var(--white); margin-bottom: 7px; }
  .brand-name {
    position: absolute; left: 0; right: 0; top: 50px;
    text-align: center;
    font-weight: 700; font-size: 20px;
    color: var(--logo-gold);
    letter-spacing: .5px;
  }
  .category-nav {
    display: flex; justify-content: space-around;
    height: 90px; padding-top: 8px;
    border-bottom: 1px solid #e3e3e3;
  }
  .category {
    width: 110px; text-align: center;
    font-size: 9px; color: var(--brand-blue); text-transform: uppercase;
  }
  .category svg { display: block; margin: 0 auto 6px; width: 64px; height: 58px; }
  .feature-colors {
    height: 120px; background: var(--blush); position: relative;
  }
  .feature-colors h2 {
    text-align: center; font-weight: 400; font-size: 36px;
    color: var(--ink); padding-top: 20px; letter-spacing: 1px;
  }
  .lipstick-row {
    position: absolute; left: 0; right: 0; bottom: 0; height: 42px;
    background: linear-gradient(90deg, var(--lip-1), #e07a8c 20%, var(--lip-2) 45%, #c23a3a 60%, #e08060 75%, var(--lip-2) 90%, #5a3a8a);
  }
  .ebook-promo {
    height: 225px; background: var(--mist); position: relative;
  }
  .ebook-promo .copy { position: absolute; left: 0; width: 370px; top: 56px; text-align: center; color: var(--brand-blue); }
  .ebook-promo .kicker { font-size: 27px; font-weight: 400; letter-spacing: .5px; }
  .ebook-promo .headline { font-size: 30px; font-weight: 700; line-height: 1.05; }
  .ebook-promo .subline { font-size: 10px; color: var(--ink); margin-top: 6px; }
  .download-button {
    display: inline-block; margin-top: 20px;
    background: var(--brand-blue); color: var(--white);
    font-size: 12px; padding: 9px 22px; border-radius: 6px;
    box-shadow: 0 0 6px var(--shadow-blue);
  }
  .ebook-cover { position: absolute; left: 372px; top: 26px; width: 86px; height: 160px; transform: skewY(-6deg); }
  .look-gallery { display: flex; height: 145px; }
  .look-gallery .look { flex: 1; }
  .look-blue { background: linear-gradient(135deg, var(--skin-1), #6a86b8 55%, var(--skin-2)); }
  .look-pink { background: linear-gradient(135deg, #e7c3c7, #d56ea5 50%, #7aa0c9); border-left: 2px solid var(--white); }
  .site-footer {
    height: 180px; background: var(--brand-blue); color: var(--white);
    font-family: "Open Sans", Arial, sans-serif;
  }
  .footer-links { display: flex; justify-content: space-around; padding: 24px 60px 0; font-size: 18px; }
  .social-row { display: flex; justify-content: center; gap: 9px; margin-top: 28px; }
  .social {
    width: 48px; height: 48px; border-radius: 50%;
    background: var(--white); color: var(--brand-blue);
    font-family: "Roboto", Arial, sans-serif; font-size: 10px; font-weight: 500;
    display: flex; align-items: center; justify-content: center;
  }
</style>
</head>
<body>
  <main class="screen">
    <header class="top-bar">
      <div class="status-bar">
        <span>●●●○○ KORVA</span>
        <span>4:21 PM</span>
        <span>22%<span class="battery"></span></span>
      </div>
      <div class="menu-toggle"><span></span><span></span><span></span></div>
      <div class="brand-name">SABINE TER HORST</div>
    </header>

    <nav class="category-nav">
      <div class="category">
        <svg viewBox="0 0 64 58"><rect width="64" height="58" fill="#3b5998"/><rect x="8" y="8" width="48" height="42" fill="none" stroke="#fff" stroke-width="2"/><line x1="18" y1="8" x2="18" y2="50" stroke="#fff" stroke-width="2"/><line x1="46" y1="8" x2="46" y2="50" stroke="#fff" stroke-width="2"/><polygon points="28,22 28,36 39,29" fill="none" stroke="#fff" stroke-width="2"/></svg>
        Tutorials
      </div>
      <div class="category">
        <svg viewBox="0 0 64 58"><rect width="64" height="58" fill="#3b5998"/><path d="M38 8 C33 16 32 20 32 23 a6 6 0 0 0 12 0 C44 20 43 16 38 8z" fill="none" stroke="#fff" stroke-width="2"/><path d="M8 40 h16 c4 0 8 2 10 4 h16 l6 -6" fill="none" stroke="#fff" stroke-width="2"/></svg>
        Skin Care
      </div>
      <div class="category">
        <svg viewBox="0 0 64 58"><rect width="64" height="58" fill="#3b5998"/><rect x="16" y="6" width="34" height="44" rx="3" fill="none" stroke="#fff" stroke-width="2"/><line x1="22" y1="16" x2="44" y2="16" stroke="#fff" stroke-width="2"/><line x1="22" y1="23" x2="44" y2="23" stroke="#fff" stroke-width="2"/><line x1="22" y1="30" x2="44" y2="30" stroke="#fff" stroke-width="2"/><line x1="22" y1="37" x2="36" y2="37" stroke="#fff" stroke-width="2"/></svg>
        Sabine's E-Book
      </div>
      <div class="category">
        <svg viewBox="0 0 64 58"><rect width="64" height="58" fill="#3b5998"/><circle cx="32" cy="22" r="10" fill="none" stroke="#fff" stroke-width="2"/><path d="M14 50 c2 -10 10 -15 18 -15 s16 5 18 15" fill="none" stroke="#fff" stroke-width="2"/></svg>
        About Sabine
      </div>
    </nav>

    <section class="feature-colors">
      <h2>LOVELY COLORS</h2>
      <div class="lipstick-row" role="img" aria-label="Row of lipsticks in pink, red, berry and violet shades"></div>
    </section>

    <section class="ebook-promo">
      <div class="copy">
        <div class="kicker">HOW TO APPLY MAKEUP</div>
        <div class="headline">LIKE THE PROS DO</div>
        <div class="subline">A Simple Guide to Common Makeup Types AND TRICKS</div>
        <span class="download-button">DOWNLOAD</span>
      </div>
      <svg class="ebook-cover" role="img" aria-label="E-book cover with makeup tools" viewBox="0 0 86 160"><defs><linearGradient id="cover" x1="0" y1="0" x2="1" y2="1"><stop offset="0" stop-color="#f4f4f6"/><stop offset="1" stop-color="#c9ccd6"/></linearGradient></defs><rect width="86" height="160" fill="url(#cover)"/><rect width="6" height="160" fill="#9aa2b8"/></svg>
    </section>

    <section class="look-gallery">
      <div class="look look-blue" role="img" aria-label="Model with blue smoky eye makeup"></div>
      <div class="look look-pink" role="img" aria-label="Model with colourful pink and blue eye makeup"></div>
    </section>

    <footer class="site-footer">
      <div class="footer-links"><span>Contact</span><span>About</span></div>
      <div class="social-row">
        <span class="social">Linkra</span>
        <span class="social">Pixora</span>
        <span class="social">Chirpa</span>
        <span class="social">Pinlo</span>
        <span class="social">Vidro</span>
      </div>
    </footer>
  </main>
</body>
</html>
```